Fresh, modern, fun business card for pediatric dental practice

Need a business card for fresh, modern, fun pediatric dental practice

Clean look that matches our website's font and colors

We prefer the look of curved corners on business cards

Target Market(s)

parents (mothers) of young children, professionals, mid-high class

Industry/Entity Type

Dental

Contact Information for Business Card

Maplebrook Pediatric Dentistry
482 Orchard Vale Road
Suite 517
Fernwick, PA 17599
555.419.3067
www.maplebrookkidsdental.example

Mara Tevlin, DMD
Colette Varnum, DMD
(we are working on our email address, but we would like that on the card as well)

Font styles to use
Sans Serif

Requirements
Must have
• All info; we would also like to make cards for individual staff members
• colors from our website and color palatte, attatched
• use same font and design as website for branding
Nice to have
• clean, simple card that has a pop of color
• we would like to see a few designs with our tag line "where smiles get brighter"
• we are not sure if we want to have it on there or not
• we would like to see a few designs incorporating the ribbon graphic on our website where the word WELCOME is

```html
<!DOCTYPE html>
<html lang="en">
<head>
<meta charset="utf-8">
<title>Maplebrook Pediatric Dentistry – Business Card</title>
<link rel="stylesheet" href="https://fonts.googleapis.com/css2?family=Roboto:wght@400;500&family=Roboto+Condensed:wght@700&display=swap">
<style>
  :root {
    --backdrop: #2b2b2b;
    --card-white: #f7f7f7;
    --brand-pink: #d12a91;
    --brand-pink-soft: #db4aa2;
    --brand-yellow: #fbb724;
    --ink-grey: #555555;
    --white: #ffffff;
  }
  * { box-sizing: border-box; margin: 0; padding: 0; }
  html, body { width: 1200px; height: 960px; overflow: hidden; }
  body {
    background: var(--backdrop);
    font-family: "Roboto", Arial, sans-serif;
    position: relative;
  }
  .card {
    position: absolute;
    left: 320px;
    width: 600px;
    height: 342px;
    border-radius: 18px;
    overflow: hidden;
  }
  .card--front { top: 105px; background: var(--card-white); }
  .card--back { top: 493px; background: var(--brand-pink); }

  /* Front */
  .front-mark {
    position: absolute;
    left: 0; right: 0; top: 112px;
    display: flex; flex-direction: column; align-items: center; gap: 14px;
  }
  .front-mark__dot {
    width: 44px; height: 44px; border-radius: 50%;
    background: var(--brand-yellow);
  }
  .front-mark__name {
    font-family: "Roboto", Arial, sans-serif;
    font-weight: 500;
    color: var(--brand-yellow);
    text-align: center;
    line-height: 1.1;
  }
  .front-mark__name-main { display: block; font-size: 40px; }
  .front-mark__name-sub { display: block; font-size: 21px; margin-top: 2px; }
  .front-web {
    position: absolute;
    left: 0; right: 0; top: 297px;
    text-align: center;
    font-size: 13px;
    letter-spacing: 3.5px;
    color: var(--ink-grey);
  }

  /* Back */
  .back-motif {
    position: absolute;
    left: 0; top: 0;
    width: 290px; height: 342px;
    background: radial-gradient(circle at 40% 45%, var(--brand-pink-soft) 0%, var(--brand-pink) 70%);
  }
  .back-info {
    position: absolute;
    right: 34px; top: 42px;
    text-align: right;
    color: var(--white);
  }
  .back-info__name {
    font-family: "Roboto", Arial, sans-serif;
    font-weight: 500;
    color: var(--brand-yellow);
    line-height: 1.1;
  }
  .back-info__name-main { display: block; font-size: 38px; }
  .back-info__name-sub { display: block; font-size: 20px; margin-top: 2px; }
  .back-info__doctors {
    margin-top: 40px;
    font-family: "Roboto Condensed", "Arial Narrow", sans-serif;
    font-weight: 700;
    font-size: 20px;
    line-height: 24px;
    color: var(--brand-yellow);
    text-transform: uppercase;
  }
  .back-info__address {
    margin-top: 6px;
    font-style: normal;
    font-size: 14.5px;
    line-height: 18.5px;
  }
  .back-info__contact { margin-top: 8px; list-style: none; font-size: 14.5px; line-height: 23px; }
  .back-info__contact li { display: flex; justify-content: flex-end; align-items: center; gap: 6px; }
  .contact-icon { width: 13px; height: 13px; fill: var(--brand-yellow); }
</style>
</head>
<body>
  <section class="card card--front" aria-label="Business card front">
    <div class="front-mark">
      <span class="front-mark__dot" aria-hidden="true"></span>
      <p class="front-mark__name">
        <span class="front-mark__name-main">Maplebrook</span>
        <span class="front-mark__name-sub">Pediatric Dentistry</span>
      </p>
    </div>
    <p class="front-web">www.maplebrookkidsdental.example</p>
  </section>

  <section class="card card--back" aria-label="Business card back">
    <div class="back-motif" role="img" aria-label="Large decorative brand motif in yellow on pink"></div>
    <div class="back-info">
      <h1 class="back-info__name">
        <span class="back-info__name-main">Maplebrook</span>
        <span class="back-info__name-sub">Pediatric Dentistry</span>
      </h1>
      <p class="back-info__doctors">Mara Tevlin, DMD<br>Colette Varnum, DMD</p>
      <address class="back-info__address">
        Maplebrook Pediatric Dentistry<br>
        482 Orchard Vale Road, Suite 517<br>
        Fernwick, PA 17599
      </address>
      <ul class="back-info__contact">
        <li>555.419.3067
          <svg class="contact-icon" viewBox="0 0 24 24" aria-hidden="true"><path d="M6.6 10.8a15.1 15.1 0 0 0 6.6 6.6l2.2-2.2c.3-.3.7-.4 1-.2 1.1.4 2.3.6 3.6.6.6 0 1 .4 1 1V20c0 .6-.4 1-1 1A17 17 0 0 1 3 4c0-.6.4-1 1-1h3.5c.6 0 1 .4 1 1 0 1.3.2 2.5.6 3.6.1.3 0 .7-.2 1z"/></svg>
        </li>
        <li>maplebrookkidsdental.example
          <svg class="contact-icon" viewBox="0 0 24 24" aria-hidden="true"><path d="M12 2a10 10 0 1 0 0 20 10 10 0 0 0 0-20zm-1 17.9A8 8 0 0 1 4.1 11H8c.1 3.3 1.1 6.4 3 8.9zM8 9H4.3A8 8 0 0 1 11 4.1 15 15 0 0 0 8 9zm5 10.9c1.9-2.5 2.9-5.6 3-8.9h3.9a8 8 0 0 1-6.9 8.9zM16 9a15 15 0 0 0-3-4.9A8 8 0 0 1 19.7 9zm-6 2h4c-.1 2.8-.9 5.4-2 7.300-1.1-1.9-1.9-4.5-2-7.3zm0-2c.2-2.1.9-4 2-5.5 1.1 1.5 1.8 3.4 2 5.5z"/></svg>
        </li>
      </ul>
    </div>
  </section>
</body>
</html>
```